banner ad

We're looking for a banner similar to the one shown on the attached file. The same 4 keywords, the same text up top, but with new formatting, design and perhaps color scheme. Looking for something to catch people's attention that will stand out on this particular page shown in the attached image. Our goal is to find a banner with a better click through rate than the current version.

```html
<!DOCTYPE html>
<html lang="en">
<head>
<meta charset="UTF-8">
<title>Blood Glucose Banner Ad</title>
<link href="https://fonts.googleapis.com/css2?family=Sansita:ital,wght@1,800&family=Open+Sans:wght@600&display=swap" rel="stylesheet">
<style>
  :root {
    --page-bg: #ffffff;
    --banner-dark: #d2500a;
    --banner-mid: #e6801f;
    --banner-warm: #efa052;
    --banner-light: #fdeedd;
    --ink: #111111;
    --ink-shadow: rgba(0, 0, 0, 0.38);
    --button-face: #ffffff;
    --button-edge: #eeeeee;
    --label-light: #ffffff;
    --chart-blue: #8fd3f0;
    --chart-green: #6fd14a;
    --chart-yellow: #f2e03a;
    --chart-orange: #f59a1c;
    --chart-red: #e2321a;
  }
  * { margin: 0; padding: 0; box-sizing: border-box; }
  html, body {
    width: 1200px;
    height: 800px;
    overflow: hidden;
    background: var(--page-bg);
  }
  .canvas {
    position: relative;
    width: 1200px;
    height: 800px;
  }
  .banner {
    position: absolute;
    left: 172px;
    top: 270px;
    width: 855px;
    height: 226px;
    overflow: hidden;
    background:
      radial-gradient(ellipse 55% 75% at 100% 0%, var(--banner-light) 0%, rgba(253,238,221,0) 72%),
      linear-gradient(110deg, var(--banner-dark) 0%, var(--banner-mid) 55%, var(--banner-warm) 100%);
  }
  .growth-visual {
    position: absolute;
    left: 18px;
    top: 28px;
    width: 192px;
    height: 192px;
    border-radius: 10px;
    background: linear-gradient(60deg,
      var(--chart-blue) 0%,
      var(--chart-green) 35%,
      var(--chart-yellow) 60%,
      var(--chart-orange) 80%,
      var(--chart-red) 100%);
    opacity: 0.9;
  }
  .headline {
    position: absolute;
    left: 230px;
    top: 6px;
    width: 590px;
    text-align: center;
    font-family: "Sansita", "Georgia", serif;
    font-style: italic;
    font-weight: 800;
    font-size: 42px;
    line-height: 56px;
    color: var(--ink);
    text-shadow: 2px 3px 3px var(--ink-shadow);
  }
  .keyword-grid {
    position: absolute;
    left: 230px;
    top: 72px;
    display: grid;
    grid-template-columns: 292px 292px;
    grid-auto-rows: 52px;
    column-gap: 16px;
    row-gap: 16px;
  }
  .keyword {
    display: flex;
    align-items: center;
    justify-content: center;
    padding-bottom: 5px;
    background: linear-gradient(180deg, var(--button-face) 0%, var(--button-edge) 100%);
    border-radius: 9px;
    box-shadow: 3px 4px 5px rgba(0, 0, 0, 0.38);
    font-family: "Sansita", "Georgia", serif;
    font-style: italic;
    font-weight: 800;
    font-size: 20.5px;
    color: var(--ink);
    text-shadow: 1px 2px 2px var(--ink-shadow);
    text-decoration: none;
    white-space: nowrap;
  }
  .ad-label {
    position: absolute;
    right: 10px;
    bottom: 5px;
    font-family: "Open Sans", Arial, sans-serif;
    font-weight: 600;
    font-size: 10.5px;
    color: var(--label-light);
  }
</style>
</head>
<body>
<div class="canvas">
  <div class="banner">
    <div class="growth-visual" role="img" aria-label="Illustration of rising coloured bars with an upward red arrow"></div>

    <h1 class="headline">Ads Related to blood glucose</h1>

    <nav class="keyword-grid">
      <a class="keyword" href="#">Blood Glucose</a>
      <a class="keyword" href="#">Blood Suger Level Chart</a>
      <a class="keyword" href="#">Normal Blood Suger Range</a>
      <a class="keyword" href="#">What is Normal Blood Suger</a>
    </nav>

    <span class="ad-label">ADVERTISEMENT</span>
  </div>
</div>
</body>
</html>
```